Tech Savy small Business accountant business card design

We need a business card for a new company based in the cloud. We provide tax, business advisory, accounting, information technology solutions and back office functions to small businesses. We offer fixed fee packages with add on services as you need them. By harnessing technology we simplify small business operational processes providing valuable time and information for small business owners to grow their business. In the logo (zulvarine) we want to be able to see zulv and experts. The final design should communicate achieving growth dreams and balance (ie life and $).
Updates
This project has been temporarily placed on hold until I finalize "Tech Savy small Business accountant needs a logo". I invite all designers to submit on this logo project. Once my logo is finalized I will resume this business card contest. Thanks Added Wednesday, March 19, 2014
This project has been temporarily placed on hold until I finalize "Tech Savy small Business accountant logo". I invite all designers to submit on this logo project. Once my logo is finalized I will resume this business card contest. Thanks Added Thursday, March 20, 2014
Target Market(s)
Small Business (Revenue $500,000, more than 3 employees) owners.
Industry/Entity Type
Small Business
Contact Information for Business Card
Marla Pennick (Principal)
Accountant, Tax Agent.
TEL | 0417 583 916
EMAIL | Marla.Pennick@zulvarine.com.au
WEB | www.zulvarine.com.au
Look and feel

```html
<!DOCTYPE html>
<html lang="en">
<head>
<meta charset="utf-8">
<title>zulvarine business card</title>
<link rel="stylesheet" href="https://fonts.googleapis.com/css2?family=Open+Sans:wght@400;600;700&display=swap">
<style>
  :root {
    --brand-blue: #0099dc;
    --band-blue: #3fb3e6;
    --ink-grey: #6d6e71;
    --silver-light: #ffffff;
    --silver-mid: #e6e7e8;
    --silver-dark: #b9babc;
    --white: #ffffff;
    --page: #ffffff;
  }
  * { box-sizing: border-box; margin: 0; padding: 0; }
  html, body {
    width: 1071px; height: 1200px; overflow: hidden;
    background: var(--page);
    font-family: "Open Sans", Arial, sans-serif;
  }
  .canvas { position: relative; width: 1071px; height: 1200px; }

  .card {
    position: absolute;
    width: 706px; height: 411px;
    overflow: hidden;
    background: linear-gradient(90deg, var(--silver-dark) 0%, var(--silver-light) 30%, var(--silver-light) 70%, var(--silver-dark) 100%);
    box-shadow: 10px 8px 10px rgba(0,0,0,0.28);
  }
  .card svg.card-shape { position: absolute; left: 0; top: 0; }

  .card--front { left: 152px; top: 100px; }
  .card--back  { left: 142px; top: 591px; border: 1px solid #9fd3ee; }

  .wordmark {
    position: absolute; left: 0; width: 100%;
    text-align: center;
    color: var(--brand-blue);
    font-weight: 700;
    letter-spacing: -1px;
    line-height: 1;
  }
  .tagline {
    position: absolute; left: 0; width: 100%;
    text-align: center;
    color: var(--ink-grey);
    line-height: 1;
  }

  .card--front .wordmark { top: 92px; font-size: 98px; }
  .card--front .tagline  { top: 186px; font-size: 27px; }
  .card--front .web-address {
    position: absolute; left: 0; width: 100%; top: 328px;
    text-align: center; color: var(--white);
    font-weight: 700; font-size: 25px; letter-spacing: 0.3px;
  }

  .card--back .wordmark { top: 31px; font-size: 48px; letter-spacing: -0.5px; }
  .card--back .tagline  { top: 88px; font-size: 14px; }

  .contact {
    position: absolute; left: 204px; top: 170px;
    color: var(--white);
  }
  .contact .name { font-size: 22px; font-weight: 700; line-height: 32px; }
  .contact .name .role { font-weight: 400; }
  .contact .title { font-size: 21px; line-height: 32px; }
  .contact .details { list-style: none; margin-top: 28px; margin-left: -32px; }
  .contact .details li {
    display: flex; align-items: center;
    font-size: 21px; line-height: 31px;
  }
  .contact .details svg { width: 22px; height: 22px; margin-right: 10px; flex: none; }
</style>
</head>
<body>
<main class="canvas">

  <section class="card card--front" aria-label="Business card front">
    <svg class="card-shape" width="706" height="411" viewBox="0 0 706 411">
      <defs>
        <linearGradient id="rule-front" x1="0" x2="1">
          <stop offset="0" stop-color="#8c8d90"/>
          <stop offset="0.5" stop-color="#e8e9ea"/>
          <stop offset="1" stop-color="#8c8d90"/>
        </linearGradient>
      </defs>
      <path d="M0,291 Q353,258 706,291 L706,300 Q353,267 0,300 Z" fill="url(#rule-front)"/>
      <path d="M0,300 Q353,267 706,300 L706,411 L0,411 Z" fill="var(--brand-blue)"/>
    </svg>
    <p class="wordmark">zulvarine</p>
    <p class="tagline">Your business and accounting partner</p>
    <p class="web-address">www.zulvarine.com.au</p>
  </section>

  <section class="card card--back" aria-label="Business card back">
    <svg class="card-shape" width="706" height="411" viewBox="0 0 706 411">
      <defs>
        <linearGradient id="rule-back" x1="0" x2="1">
          <stop offset="0" stop-color="#8c8d90"/>
          <stop offset="0.5" stop-color="#e8e9ea"/>
          <stop offset="1" stop-color="#8c8d90"/>
        </linearGradient>
      </defs>
      <path d="M0,112 Q353,100 706,112 L706,122 Q353,110 0,122 Z" fill="url(#rule-back)"/>
      <path d="M0,122 Q353,110 706,122 L706,411 L0,411 Z" fill="var(--brand-blue)"/>
      <rect class="accent-band" x="628" y="125" width="22" height="286" fill="var(--band-blue)"/>
    </svg>
    <p class="wordmark">zulvarine</p>
    <p class="tagline">Your business and accounting partner</p>

    <div class="contact">
      <p class="name">Marla Pennick <span class="role">(Principal)</span></p>
      <p class="title">Accountant, Tax Agent</p>
      <ul class="details">
        <li>
          <svg viewBox="0 0 24 24" aria-hidden="true"><path d="M7 2 L10 6 L8 9 Q10 14 14 17 L16 15 L20 18 L17 22 Q9 20 5 10 Q4 5 7 2 Z" fill="none" stroke="#fff" stroke-width="1.6" stroke-linejoin="round"/></svg>
          0417 583 916
        </li>
        <li>
          <svg viewBox="0 0 24 24" aria-hidden="true"><rect x="2" y="5" width="20" height="14" fill="none" stroke="#fff" stroke-width="1.6"/><path d="M2 5 L12 13 L22 5" fill="none" stroke="#fff" stroke-width="1.6"/></svg>
          Marla.Pennick@zulvarine.com.au
        </li>
        <li>
          <svg viewBox="0 0 24 24" aria-hidden="true"><circle cx="12" cy="12" r="9.5" fill="none" stroke="#fff" stroke-width="1.5"/><ellipse cx="12" cy="12" rx="4.5" ry="9.5" fill="none" stroke="#fff" stroke-width="1.3"/><path d="M2.5 12 H21.5 M4 7 H20 M4 17 H20" stroke="#fff" stroke-width="1.2"/></svg>
          www.zulvarine.com.au
        </li>
      </ul>
    </div>
  </section>

</main>
</body>
</html>
```